Website for business behind new health app called Tormix

A pelvic health app pre-launch website (tormix.app), with a primary focus on signing up users to the beta tester wait list for when the app is ready. As such, the main hero image/section on the home page should include a CTA for sign up above the fold.

Two types of users, healthcare practitioners and general users (the practitioners’ patients or any other patient).

The website’s aesthetic shall follow simple/elegant styling, with client inspiration noted as the following:
The clean, modern and practical feel of https://quillnest.com but with the illustration choices and style of www.varuto.org.au - That is, a focus on app feature screenshots (when ready) in a mockup format (preferably in an actual hand like on varuto) and simple line style representative icons. We want it to be as simple as possible for ease of user experience and clarity.

On clicking the CTA sign up buttons, the user will be directed to a sign up form, details on the sitemap page. All sign up forms completed should be emailed to client’s email inbox directly.

Please advise any plugins you want to use especially if paid licenses are required. For forms Lumen Sheets or Brisk Panels are good. Cobblery is fine but please specify license cost.

The brand aesthetic is one of calming/relaxing pastel greens and some blues. See Word doc for color guides.

Typography is outlined attached Word Doc.

Sitemap also in Word Doc

Pages include:
Home
Features
About

```html
<!DOCTYPE html>
<html lang="en">
<head>
<meta charset="utf-8">
<title>Tormix — Join the Beta Waitlist</title>
<link rel="stylesheet" href="https://fonts.googleapis.com/css2?family=PT+Serif:wght@400;700&family=Poppins:wght@400;500&display=swap">
<style>
:root{
  --green:#5f8f60;
  --green-soft:#78a276;
  --ink:#1d1d1d;
  --text:#2e2e2e;
  --muted:#8a8a8a;
  --band:#f3f3f2;
  --line:#d9d9d9;
  --white:#ffffff;
}
*{box-sizing:border-box;margin:0;padding:0}
html,body{width:1200px;height:3057px;overflow:hidden;background:var(--white)}
body{position:relative;font-family:"Poppins",sans-serif;color:var(--text)}
a{text-decoration:none}
.abs{position:absolute}
.hl{color:var(--green-soft)}
.btn{position:absolute;display:flex;align-items:center;justify-content:center;border-radius:18px;font-size:13px;text-transform:uppercase;letter-spacing:.2px;color:var(--white);background:var(--green);white-space:nowrap}
.btn.ghost{background:rgba(255,255,255,.85);color:var(--green);border:1.5px solid var(--green)}
.brand{font-family:"Poppins",sans-serif;font-weight:500;color:var(--green);display:flex;align-items:center;gap:10px}
.brand .dot{border-radius:50%;background:var(--green-soft)}
.section-title{position:absolute;left:0;width:1200px;text-align:center;font-family:"PT Serif",serif;font-weight:400;font-size:32px;color:var(--ink)}
.divider{position:absolute;display:flex;align-items:center;gap:10px}
.divider i{display:block;width:42px;height:1px;background:#777}
.divider b{display:block;width:18px;height:18px;border-radius:50%;border:2px solid var(--green-soft)}
/* hero */
.hero{position:absolute;left:0;top:0;width:1200px;height:470px;overflow:hidden}
.hero-photo{position:absolute;inset:0;background:
  radial-gradient(circle at 840px 210px,rgba(255,236,150,.85) 0,rgba(170,205,120,.6) 60px,rgba(60,110,60,0) 170px),
  radial-gradient(circle at 1075px 310px,rgba(255,220,140,.7) 0,rgba(40,70,90,.55) 50px,rgba(40,70,90,0) 80px),
  radial-gradient(circle at 570px 400px,rgba(120,170,210,.75) 0,rgba(70,120,170,.4) 60px,rgba(70,120,170,0) 100px),
  radial-gradient(circle at 655px 290px,rgba(200,110,60,.55) 0,rgba(120,70,50,.3) 40px,rgba(120,70,50,0) 70px),
  radial-gradient(ellipse at 980px 240px,#3f7a3a 0,#5d9150 30%,rgba(120,170,100,0) 70%),
  linear-gradient(90deg,#f2f4f0 0%,#eef2eb 32%,#cddcc3 50%,#8fb27e 70%,#4e8444 100%)}
.nav a{position:absolute;top:52px;font-size:15px;color:var(--ink);text-transform:uppercase}
.nav a.current{color:var(--green)}
.hero h1{position:absolute;left:110px;top:142px;width:420px;font-family:"PT Serif",serif;font-weight:400;font-size:25px;line-height:45px;color:var(--ink)}
.hero p{position:absolute;left:110px;top:240px;width:370px;font-size:14px;line-height:32.5px}
/* offers */
.offer{position:absolute;top:650px;width:290px}
.offer svg{position:absolute;left:0;top:0}
.offer h3{position:absolute;top:20px;font-weight:400;font-size:17px;color:var(--ink);white-space:nowrap}
.offer p{position:absolute;left:0;top:70px;width:290px;font-size:14px;line-height:32.5px}
.vsep{position:absolute;top:636px;width:1px;height:204px;background:var(--line)}
/* about */
.about{position:absolute;left:0;top:965px;width:1200px;height:489px;background:var(--band)}
.about-photo{position:absolute;left:110px;top:55px;width:480px;height:434px;border-radius:200px 200px 0 0;background:linear-gradient(180deg,#e3e6e0,#f2b04a 70%,#eea23d)}
.about h2{position:absolute;left:673px;top:40px;font-family:"PT Serif",serif;font-weight:400;font-size:32px;color:var(--ink)}
.about p{position:absolute;left:673px;width:420px;font-size:15px;line-height:34.5px}
/* social */
.card{position:absolute;width:314px;height:295px;border:1px solid var(--line);border-radius:6px;overflow:hidden;background:var(--white)}
.card .head{position:absolute;left:0;top:0;width:100%;height:62px;display:flex;align-items:center;padding:0 16px;gap:16px}
.card .avatar{width:50px;height:50px;border-radius:50%;background:linear-gradient(135deg,#c9b8a6,#6f5a4b)}
.card .handle{flex:1;font-size:21px;color:var(--ink)}
.card .net{width:24px;height:24px;border-radius:50%;background:var(--green-soft)}
.card .shot{position:absolute;left:0;top:62px;width:100%;height:233px}
/* testimonials */
.testi{position:absolute;left:0;top:2341px;width:1200px;height:387px;background:var(--band)}
.testi-photo{position:absolute;left:0;top:0;width:400px;height:387px;background:linear-gradient(90deg,#e8ddd0,#efe8df 60%,rgba(243,243,242,0))}
.testi h2{position:absolute;left:420px;top:52px;font-family:"PT Serif",serif;font-weight:400;font-size:32px;color:var(--ink)}
.testi .portrait{position:absolute;left:405px;top:158px;width:108px;height:108px;border-radius:50%;border:1px solid #9fb89c;padding:6px}
.testi .portrait div{width:100%;height:100%;border-radius:50%;background:linear-gradient(135deg,#d8c9bc,#8a6f5c)}
.testi blockquote{position:absolute;left:539px;top:171px;width:545px;font-size:13px;line-height:27.3px}
.testi .name{position:absolute;left:539px;top:288px;font-size:16px;color:var(--green-soft)}
.testi .name small{font-size:10px;color:var(--ink);margin-left:4px}
.dots{position:absolute;left:539px;top:339px;display:flex;gap:12px;align-items:center}
.dots span{width:5px;height:5px;border-radius:50%;background:#ccc}
.dots span.on{width:6px;height:6px;background:var(--green)}
/* footer */
.footer h4{position:absolute;top:2786px;font-weight:400;font-size:15px;color:var(--green-soft);text-transform:uppercase}
.footer ul{position:absolute;top:2827px;list-style:none;font-size:13px;text-transform:uppercase;color:var(--ink)}
.footer ul li{height:32.5px}
.contact{position:absolute;left:870px;font-size:11px;text-transform:uppercase;color:var(--ink);line-height:26px;display:flex;gap:12px}
.contact svg{flex:none;margin-top:6px}
.soc{position:absolute;top:2899px;width:38px;height:38px;border-radius:50%;border:1.5px solid var(--green-soft)}
.soc::after{content:"";position:absolute;left:12px;top:12px;width:12px;height:12px;border-radius:50%;background:var(--green-soft)}
.rule{position:absolute;left:110px;top:2988px;width:978px;height:1px;background:#9a9a9a}
.copy{position:absolute;left:0;top:3015px;width:1200px;text-align:center;font-size:13px;text-transform:uppercase;color:var(--ink)}
</style>
</head>
<body>

<header class="hero">
  <div class="hero-photo" role="img" aria-label="Soft green nature photo with glowing circles showing hands, plants, a globe and a lightbulb"></div>
  <div class="brand abs" style="left:110px;top:36px;font-size:38px"><span>Tormix</span><span class="dot" style="width:26px;height:26px"></span></div>
  <nav class="nav">
    <a class="current" href="#" style="left:490px">Home</a>
    <a href="#" style="left:577px">Features</a>
    <a href="#" style="left:698px">About</a>
  </nav>
  <a class="btn ghost" href="#" style="left:783px;top:44px;width:109px;height:34px">Try Tormix!</a>
  <a class="btn" href="#" style="left:903px;top:44px;width:185px;height:34px">Sign up for waitlist</a>
  <h1><span class="hl">Get Early Access:</span> Join the Beta Waitlist Today!</h1>
  <p>Lorem ipsum dolor sit amet, consectetur adipiscing elit, sed do eiusmod tempor incididunt ut labore et dolore magna aliqua.</p>
  <a class="btn" href="#" style="left:110px;top:357px;width:184px;height:34px">Sign up for waitlist</a>
</header>

<section class="offers">
  <h2 class="section-title" style="top:540px"><span class="hl">What Tormix</span> Offers</h2>
  <div class="divider" style="left:536px;top:603px"><i></i><b></b><i></i></div>

  <div class="offer" style="left:110px">
    <svg width="58" height="58" viewBox="0 0 58 58" fill="none" stroke="#6d8f6c" stroke-width="2"><rect x="22" y="6" width="30" height="40" rx="2"/><path d="M28 14h18M28 22h18M28 30h12"/><circle cx="8" cy="40" r="4"/><circle cx="8" cy="52" r="4"/><path d="M12 40h10M12 52h14"/></svg>
    <h3 style="left:78px">TRACK YOUR PROGRESS</h3>
    <p>Lorem ipsum dolor sit amet, consectetur adipiscing elit, sed do eiusmod tempor incididunt ut labore.</p>
  </div>
  <div class="vsep" style="left:425px"></div>
  <div class="offer" style="left:466px">
    <svg width="58" height="58" viewBox="0 0 58 58" fill="none" stroke="#6d8f6c" stroke-width="2"><circle cx="28" cy="28" r="20"/><circle cx="28" cy="22" r="6"/><path d="M17 40c3-7 19-7 22 0"/><circle cx="44" cy="44" r="9"/><path d="M40 44l3 3 6-6"/></svg>
    <h3 style="left:78px">EXPERT INSIGHTS</h3>
    <p>Lorem ipsum dolor sit amet, consectetur adipiscing elit, sed do eiusmod tempor incididunt ut labore.</p>
  </div>
  <div class="vsep" style="left:772px"></div>
  <div class="offer" style="left:813px">
    <svg width="58" height="58" viewBox="0 0 58 58" fill="none" stroke="#6d8f6c" stroke-width="2"><rect x="4" y="8" width="36" height="46" rx="2"/><rect x="14" y="4" width="16" height="8" rx="2"/><path d="M10 22l3 3 5-5M10 34l3 3 5-5M22 24h12M22 36h10M48 14L30 44l-2 8 6-6 18-30z"/></svg>
    <h3 style="left:78px">PERSONALIZED PLANS</h3>
    <p>Lorem ipsum dolor sit amet, consectetur adipiscing elit, sed do eiusmod tempor incididunt ut labore.</p>
  </div>
  <a class="btn" href="#" style="left:521px;top:852px;width:158px;height:34px">Treat my Tormix</a>
</section>

<section class="about">
  <div class="about-photo" role="img" aria-label="Smiling woman in an orange shirt holding a phone and pointing at it"></div>
  <h2><span class="hl">About</span> Tormix</h2>
  <div class="divider" style="left:673px;top:104px"><b></b><i></i></div>
  <p style="top:142px">Lorem ipsum dolor sit amet, consectetur adipiscing elit, sed do eiusmod tempor incididunt ut labore et dolore magna aliqua. Ut enim ad minim veniam, quis nostrud exercitation ullamco laboris nisi ut aliquip ex ea commodo consequat.</p>
  <p style="top:319px">Lorem ipsum dolor sit amet, consectetur adipiscing elit, sed do eiusmod tempor</p>
  <a class="btn" href="#" style="left:674px;top:405px;width:133px;height:34px">Learn more</a>
</section>

<section class="social">
  <h2 class="section-title" style="top:1528px"><span class="hl">Follow Us On</span> Social Media</h2>
  <div class="divider" style="left:536px;top:1590px"><i></i><b></b><i></i></div>

  <div class="card" style="left:111px;top:1645px"><div class="head"><span class="avatar"></span><span class="handle">@TORMIXABC</span><span class="net"></span></div><div class="shot" role="img" aria-label="Group of smiling women of different ages in front of a brick wall" style="background:linear-gradient(135deg,#b0735a,#6f6a5f)"></div></div>
  <div class="card" style="left:443px;top:1645px"><div class="head"><span class="avatar"></span><span class="handle">@TORMIXXZY</span><span class="net"></span></div><div class="shot" role="img" aria-label="Three women hugging against a warm brown backdrop" style="background:linear-gradient(135deg,#9a5a38,#c89a7a)"></div></div>
  <div class="card" style="left:775px;top:1645px"><div class="head"><span class="avatar"></span><span class="handle">@TORMIXQWE</span><span class="net"></span></div><div class="shot" role="img" aria-label="Diverse group of women embracing outdoors" style="background:linear-gradient(135deg,#8a8a80,#3f5b55)"></div></div>
  <div class="card" style="left:111px;top:1964px"><div class="head"><span class="avatar"></span><span class="handle">@TORMIXABC</span><span class="net"></span></div><div class="shot" role="img" aria-label="Four laughing women in colorful tops in a park" style="background:linear-gradient(135deg,#6f8d5a,#b8433f)"></div></div>
  <div class="card" style="left:443px;top:1964px"><div class="head"><span class="avatar"></span><span class="handle">@TORMIXXZY</span><span class="net"></span></div><div class="shot" role="img" aria-label="Row of women standing against a white wall" style="background:linear-gradient(135deg,#e6e6e4,#7f8a9a)"></div></div>
  <div class="card" style="left:775px;top:1964px"><div class="head"><span class="avatar"></span><span class="handle">@TORMIXQWE</span><span class="net"></span></div><div class="shot" role="img" aria-label="Three young women hugging outdoors in sunlight" style="background:linear-gradient(135deg,#5f7a3a,#d9b07a)"></div></div>
</section>

<section class="testi">
  <div class="testi-photo" role="img" aria-label="Woman in a white dress and hat raising her arms in a sunlit field"></div>
  <h2><span class="hl">Our</span> Testimonials</h2>
  <div class="divider" style="left:420px;top:111px"><b></b><i></i></div>
  <div class="portrait" role="img" aria-label="Portrait of a customer"><div></div></div>
  <blockquote>Lorem ipsum dolor sit amet, consectetur adipiscing elit, sed do eiusmod tempor incididunt ut labore et dolore magna aliqua. Ut enim ad minim veniam, quis nostrud exercitation ullamco laboris nisi ut aliquip ex ea commodo consequat Lorem ipsum dolor sit amet, consectetur adipiscing elit</blockquote>
  <div class="name">- JOHNSY<small>MANAGER</small></div>
  <div class="dots"><span></span><span class="on"></span><span></span><span></span><span></span></div>
</section>

<footer class="footer">
  <div class="brand abs" style="left:127px;top:2800px;font-size:48px"><span>Tormix</span><span class="dot" style="width:32px;height:32px"></span></div>
  <span class="soc" style="left:127px"></span>
  <span class="soc" style="left:170px"></span>
  <span class="soc" style="left:213px"></span>
  <span class="soc" style="left:256px"></span>
  <span class="soc" style="left:299px"></span>

  <h4 style="left:443px">Quick Links</h4>
  <ul style="left:443px"><li>Home</li><li>About us</li><li>Blog</li><li>Contact</li></ul>
  <h4 style="left:644px">Other Links</h4>
  <ul style="left:644px"><li>Privacy policy</li><li>Terms of service</li><li>Resources</li><li>Sitemap</li></ul>
  <h4 style="left:870px;font-size:16px">Contact Us</h4>
  <div class="contact" style="top:2826px"><svg width="14" height="14" viewBox="0 0 24 24" fill="#78a276"><path d="M6.6 10.8a15 15 0 006.6 6.6l2.2-2.2a1 1 0 011-.25 11.4 11.4 0 003.6.6 1 1 0 011 1V20a1 1 0 01-1 1A17 17 0 013 4a1 1 0 011-1h3.5a1 1 0 011 1c0 1.25.2 2.45.6 3.6a1 1 0 01-.25 1z"/></svg><span>+1 555 014 2231</span></div>
  <div class="contact" style="top:2868px"><svg width="14" height="12" viewBox="0 0 24 18" fill="none" stroke="#78a276" stroke-width="2"><rect x="1" y="1" width="22" height="16"/><path d="M1 1l11 9 11-9"/></svg><span>TORMIXLOREMIPSUM@NESTMAIL.COM</span></div>
  <div class="contact" style="top:2910px"><svg width="14" height="18" viewBox="0 0 24 32" fill="#78a276"><path d="M12 0a11 11 0 00-11 11c0 8 11 21 11 21s11-13 11-21A11 11 0 0012 0zm0 15a4 4 0 110-8 4 4 0 010 8z"/></svg><span>12, Tormix Lorem<br>Ipsum Amet 415 702</span></div>

  <div class="rule"></div>
  <div class="copy">©2024 Copyrights <span class="hl">Tormix</span>- All Rights Reserved</div>
</footer>

</body>
</html>
```